Webdesign for Dutch IT consultancy company

Make a Wordpress webdesign for a Dutch consultancy company

Briefing Velmora IT

Website for finding and connecting IT-professionals. Corebusiness is to find IT-professionals and to help them to follow their ambitions. We offer training, personal coaching and education trajects.

U can take www.Tralvique.nl as an example for the website.

Home page

U can take www.Tralvique.nl as an example.

There should be jobs on the home page. A block for short info about us and about what whe do and a trigger to contact us quickly.

Jobs Page

On this page should be the jobs that we offer for the professionals. There should be a search function on this page so u can easily find the job that you are looking for.

A call to action can be on this page too.

Also a little block with text for some information.

For professionals page

Block with information on top. Call to action. info about who we work for/with.

For Clients

Info about three different solutions

- Sourcing solutions
- Consultancy solutions
- Custom based traineeships

Request a qoute option

Traineeships page

Info about two different traineeships

- Linux traineeships
- Microsoft traineeships

Call to action/ subscribe for traineeships

About us page

We are Velmora IT

Our mission: Creating cooperations between young professionals and businesses who wanna work on a great future.

Our core values

Last news

Target Market(s)

Young professionals and businesses who need IT services

Industry/Entity Type

It Company

Coding

Coded - Design and coding required

Number of Pages Required

5+ page

Font styles to use
Other font styles liked:
• Calibri

Colors
ffffff
add136
6b449b

Requirements
Must have
• Home page, Jobs Page, Professionals page, Clients page, Traineeships page, About us Page
• Green and/or Purple layout. Job search option, subscribe option
Nice to have
• modern design

```html
<!DOCTYPE html>
<html lang="en">
<head>
<meta charset="utf-8">
<title>Website Designer – Velmora IT</title>
<link rel="stylesheet" href="https://fonts.googleapis.com/css2?family=Varela+Round&family=Open+Sans:wght@400;600&display=swap">
<style>
:root{
  --purple:#6b449b;
  --green:#add136;
  --band-green:#7dc246;
  --btn-green:#78b943;
  --red:#f0606d;
  --text:#707070;
  --heading:#444;
  --line:#e4e4e4;
  --title-bg:#f7f7f7;
  --footer-bg:#5e5e5e;
  --footer-bar:#525252;
  --white:#fff;
}
*{box-sizing:border-box;margin:0;padding:0}
html,body{width:1200px;height:3093px;overflow:hidden}
body{font-family:"Open Sans",sans-serif;color:var(--text);background:var(--white);font-size:12px;line-height:17.6px;position:relative}
h1,h2,h3,h4,.nav{font-family:"Varela Round",sans-serif}
a{color:inherit;text-decoration:none}
ul{list-style:none}

.site-header{position:absolute;top:0;left:0;width:1200px;height:82px;border-bottom:1px solid var(--line);background:var(--white)}
.brand{font-family:"Open Sans",sans-serif;font-weight:600;color:var(--heading);letter-spacing:1px}
.site-header .brand{position:absolute;left:165px;top:24px;font-size:24px;line-height:30px}
.nav{position:absolute;right:163px;top:26px;display:flex;align-items:center;gap:28px;font-size:12.5px;color:#555}
.nav .caret{font-size:9px}
.nav .login{border:1px solid #555;border-radius:3px;padding:7px 11px}

.title-band{position:absolute;top:82px;left:0;width:1200px;height:145px;background:var(--title-bg);border-bottom:1px solid var(--line);text-align:center}
.title-band h1{font-size:26px;font-weight:400;color:#444;margin-top:44px}
.job-meta{display:flex;justify-content:center;gap:22px;margin-top:18px;font-size:11px;color:#555;line-height:15px}
.job-meta span{display:flex;align-items:center;gap:5px}
.badge{background:var(--red);color:var(--white);font-size:8.5px;font-weight:600;text-transform:uppercase;padding:2px 8px;border-radius:2px;line-height:12px}
.badge.full{background:#57b846}

.main{position:absolute;top:227px;left:173px;width:854px;height:2126px}
.content{position:absolute;left:0;top:48px;width:709px}
.content h2{font-size:16px;font-weight:400;color:var(--heading);margin-bottom:14px;line-height:20px}
.content h3{font-size:14.5px;font-weight:400;color:var(--heading);margin:0 0 12px;line-height:20px}
.content h2.section{font-size:17px;margin:44px 0 16px}
.content h3.sub{margin-top:30px}
.content p{margin-bottom:17px}
.hero-image{width:709px;height:221px;background:linear-gradient(120deg,#4f5a64 0%,#c9c3b8 40%,#e8e6e1 60%,#3d444b 100%);margin-bottom:26px}
.bullets li{position:relative;padding-left:28px}
.bullets li::before{content:"";position:absolute;left:14px;top:7px;width:4px;height:4px;border-radius:50%;background:#555}
.btn-apply{display:inline-block;border:2px solid var(--btn-green);color:var(--btn-green);font-size:10px;font-weight:600;text-transform:uppercase;padding:9px 18px;border-radius:3px;margin-top:22px;line-height:14px}

.sidebar{position:absolute;left:730px;top:47px;width:124px}
.company-logo{width:124px;height:124px;background:#efefef;display:flex;align-items:center;justify-content:center;font-family:"Open Sans",sans-serif;color:var(--heading);font-size:18px}
.sidebar .badge{display:block;text-align:center;margin-top:33px}
.sidebar .btn-apply{width:124px;text-align:center;margin-top:22px;padding:10px 0}
.sidebar h4{font-size:16px;font-weight:400;color:var(--heading);text-align:center;margin-top:28px;line-height:20px;padding:0 10px}
.social{margin-top:10px}
.social li{font-size:11px;line-height:17px;display:flex;align-items:center;gap:6px}
.social .ico{width:9px;height:9px;border-radius:2px;background:#999}
.tag{margin-top:28px;font-size:11px;display:flex;align-items:center;gap:6px}

.related{position:absolute;left:0;top:1791px;width:854px}
.related h2{font-size:17px;font-weight:400;color:var(--heading);margin-bottom:16px}
.job-list{border:1px solid var(--line);border-radius:3px}
.job-row{height:76px;display:flex;align-items:center;border-bottom:1px solid var(--line);position:relative}
.job-row:last-child{border-bottom:0}
.job-row .logo-box{width:48px;height:48px;background:#f0f0f0;margin-left:12px;display:flex;align-items:center;justify-content:center;font-size:10px;color:#555}
.job-row .info{position:absolute;left:79px;line-height:16px}
.job-row .info strong{display:block;font-weight:400;font-size:13px;color:#444}
.job-row .info small{font-size:10.5px;color:#666}
.job-row .info small b{font-weight:600;color:#444}
.job-row .loc{position:absolute;left:448px;font-size:12px;display:flex;align-items:center;gap:5px;color:#555}
.job-row .status{position:absolute;left:666px;width:165px;text-align:center;font-size:10px;line-height:14px}
.job-row .status .badge{display:block;margin-bottom:2px}

.question-band{position:absolute;top:2353px;left:0;width:1200px;height:165px;background:var(--band-green);color:var(--white);text-align:center}
.question-band h2{font-weight:400;font-size:30px;margin-top:48px;line-height:36px}
.question-band p{font-size:11px;margin-top:18px}

.site-footer{position:absolute;top:2518px;left:0;width:1200px;height:534px;background:var(--footer-bg);color:#e8e8e8;font-size:11px;line-height:17.5px}
.footer-col{position:absolute;top:74px}
.footer-col h4{font-weight:400;font-size:16px;color:var(--white);margin-bottom:12px;line-height:20px}
.footer-brand{left:173px;width:190px;top:82px}
.footer-brand .brand{font-size:22px;line-height:26px;color:var(--white);margin-bottom:18px}
.sitemap{left:392px}
.sitemap li::before{content:"•";margin-right:6px}
.news{left:612px;width:190px}
.news li{margin-bottom:8px}
.news small{display:block;font-size:9px;color:#ccc;line-height:12px}
.offices{left:831px;width:200px}
.offices p{margin-bottom:14px}

.footer-bar{position:absolute;top:3052px;left:0;width:1200px;height:41px;background:var(--footer-bar);color:#ccc;font-size:8.5px;text-transform:uppercase}
.footer-bar .copy{position:absolute;left:173px;top:12px}
.footer-bar .top{position:absolute;left:594px;top:13px;width:13px;height:13px;border-radius:50%;background:#ccc}
.footer-bar .icons{position:absolute;right:173px;top:16px;display:flex;gap:13px}
.footer-bar .icons span{width:9px;height:9px;border-radius:50%;background:#ccc}
</style>
</head>
<body>

<header class="site-header">
  <div class="brand">VELMORA IT</div>
  <nav class="nav">
    <a>Find A Job <span class="caret">▾</span></a>
    <a>Post A Job</a>
    <a>Pages <span class="caret">▾</span></a>
    <a>Blog</a>
    <a>Shop <span class="caret">▾</span></a>
    <a>Sign Up</a>
    <a class="login">Login</a>
  </nav>
</header>

<section class="title-band">
  <h1>Website Designer</h1>
  <div class="job-meta">
    <span class="badge">Freelance</span>
    <span><svg width="8" height="10" viewBox="0 0 8 10"><path d="M4 0a4 4 0 0 0-4 4c0 3 4 6 4 6s4-3 4-6a4 4 0 0 0-4-4zm0 5.5A1.5 1.5 0 1 1 4 2.5a1.5 1.5 0 0 1 0 3z" fill="#555"/></svg>Pickering, Ontario</span>
    <span><svg width="10" height="10" viewBox="0 0 10 10"><rect x=".5" y="1.5" width="9" height="8" fill="none" stroke="#555"/><line x1="0" y1="4" x2="10" y2="4" stroke="#555"/></svg>Posted 4 years ago</span>
    <span><svg width="9" height="9" viewBox="0 0 9 9"><rect x="1" y="3" width="7" height="6" fill="#555"/><path d="M4.5 0L9 3H0z" fill="#555"/></svg>Pinhaven</span>
  </div>
</section>

<main class="main">
  <article class="content">
    <h2>Overview</h2>
    <div class="hero-image" role="img" aria-label="Photo of designers working at computers in a bright office"></div>

    <h3>Company Description</h3>
    <p>Company is a 2016 Iowa City-born start-up that develops consectetuer adipiscing elit. Phasellus hendrerit. Pellentesque aliquet nibh nec urna. In nisi neque, aliquet vel, dapibus id, mattis vel, nisi. Sed pretium, ligula sollicitudin laoreet viverra, tortor libero sodales leo, eget blandit nunc tortor eu nibh. Nullam mollis. Ut justo. Suspendisse potenti.</p>
    <p>Sed egestas, ante et vulputate volutpat, eros pede semper est, vitae luctus metus libero eu augue. Morbi purus libero, faucibus adipiscing, commodo quis, gravida id, est. Sed lectus. Praesent elementum hendrerit tortor. Sed semper lorem at felis. Vestibulum volutpat, lacus a ultrices sagittis, mi neque euismod dui, eu pulvinar nunc sapien ornare nisl. Phasellus pede arcu, dapibus eu, fermentum et, dapibus sed, urna.</p>
    <p>Morbi interdum mollis sapien. Sed ac risus. Phasellus lacinia, magna a ullamcorper laoreet, lectus arcu pulvinar risus, vitae facilisis libero dolor a purus. Sed vel lacus. Mauris nibh felis, adipiscing varius, adipiscing in, lacinia vel, tellus. Suspendisse ac urna. Etiam pellentesque mauris ut lectus. Nunc tellus ante, mattis eget, gravida vitae, ultricies ac, leo. Integer leo pede, ornare a, lacinia eu, vulputate vel, nisl.</p>
    <p>Suspendisse mauris. Fusce accumsan mollis eros. Pellentesque a diam sit amet mi ullamcorper vehicula. Integer adipiscing risus a sem. Nullam quis massa sit amet nibh viverra malesuada. Nunc sem lacus, accumsan quis, faucibus non, congue vel, arcu. Ut scelerisque hendrerit tellus. Integer sagittis. Vivamus a mauris eget arcu gravida tristique. Nunc iaculis mi in ante. Vivamus imperdiet nibh feugiat est.</p>

    <h2 class="section">Job Description</h2>
    <p>As Marketing Graphic Designer, your primary responsibility is to assist the Marketing and Social Media team with a variety of graphic design tasks ranging from email, ads, print, and website design. You will be responsible to take a set of instructions, or a stated problem, and produce clean, modern design assets that are within the brand requirements of our company and our products. As part of the process, this person will collaborate with members of the marketing, design and product teams to gain a clear understanding of the campaign expectations, target audience, and product positioning.</p>
    <p>The right candidate will possess video production and editing skills. You will work with the marketing and social media team in the video production cycle from pre-production planning through post-production editing (video training available).</p>
    <p>Design work will be completed in a timely fashion, largely unsupervised short of regular design feedback, and meet the stated requirements of the requestor/stakeholder.</p>
    <p>For website design, a basic level of coding is required in order to turn designs into live websites.</p>

    <h3 class="sub">Key Objectives</h3>
    <ul class="bullets">
      <li>Take a set of instructions or a stated problem and produce clean, modern design assets that are within the brand requirements of our company and our products.</li>
    </ul>

    <h3 class="sub">Primary Areas of Accountability</h3>
    <ul class="bullets">
      <li>Collaborate with the Marketing Manager to deliver effective, direct response e-mail designs for marketing campaigns</li>
      <li>Work with stakeholders from sales and marketing to design print materials, including sales brochures and mailers</li>
      <li>Work closely with the CMO and in-house design team, taking direction on our new website design for corporate and product sites, including writing HTML and CSS</li>
      <li>Work closely with the CMO and in-house design team to compile the corporate and product family branding style guides (icons, color palettes, etc)</li>
      <li>Develop design assets for new product launches, including screenshots and icons for app store listings</li>
      <li>Design on request for various needs across the company, including graphics for e-books, online stores, social accounts, presentations, ads, collateral, etc.</li>
    </ul>

    <h3 class="sub">Required Knowledge, Skills, and Abilities</h3>
    <ul class="bullets">
      <li>Ability to write code – HTML &amp; CSS (SCSS flavor of SASS preferred when writing CSS)</li>
      <li>Proficient in PixelForge, VectorLab, bonus points for familiarity with Drafta (Drafta is our preferred concepting tool)</li>
      <li>Cross-browser and platform testing as standard practice</li>
      <li>Experience using Protoly a plus</li>
      <li>Experience in video production a plus or, at a minimum, a willingness to learn</li>
    </ul>

    <h3 class="sub">Education + Experience</h3>
    <ul class="bullets">
      <li>Advanced degree or equivalent experience in graphic and web design</li>
      <li>3 or more years of professional design experience</li>
      <li>Direct response email experience</li>
      <li>Ecommerce website design experience</li>
      <li>Familiarity with mobile and web apps preferred</li>
      <li>Excellent communication skills, most notably a demonstrated ability to solicit and address creative and design feedback</li>
      <li>Must be able to work under pressure and meet deadlines while maintaining a positive attitude and providing exemplary customer service</li>
      <li>Ability to work independently and to carry out assignments to completion within parameters of instructions given, prescribed routines, and standard accepted practices</li>
    </ul>

    <a class="btn-apply">Apply for job</a>
  </article>

  <aside class="sidebar">
    <div class="company-logo">Pinhaven</div>
    <span class="badge">Freelance</span>
    <a class="btn-apply">Apply for job</a>
    <h4>Company Social</h4>
    <ul class="social">
      <li><span class="ico"></span>Website</li>
      <li><span class="ico"></span>Chirpline</li>
      <li><span class="ico"></span>Friendpage</li>
      <li><span class="ico"></span>Worklinked</li>
    </ul>
    <div class="tag"><svg width="9" height="9" viewBox="0 0 9 9"><path d="M0 0h5l4 4-5 5-4-4z" fill="#777"/></svg>Design</div>
  </aside>

  <section class="related">
    <h2>Related Jobs</h2>
    <div class="job-list">
      <div class="job-row">
        <div class="logo-box">Tablora</div>
        <div class="info"><strong>Web Designer / Front End Developer</strong><small><b>Tablora</b></small></div>
        <div class="loc"><svg width="9" height="12" viewBox="0 0 8 10"><path d="M4 0a4 4 0 0 0-4 4c0 3 4 6 4 6s4-3 4-6a4 4 0 0 0-4-4zm0 5.5A1.5 1.5 0 1 1 4 2.5a1.5 1.5 0 0 1 0 3z" fill="#555"/></svg>Kearney, Missouri</div>
        <div class="status"><span class="badge">Freelance</span>Posted 5 years ago</div>
      </div>
      <div class="job-row">
        <div class="logo-box">Stride</div>
        <div class="info"><strong>User Experience Designer</strong><small><b>Stridewell</b> Motion made simple</small></div>
        <div class="loc"><svg width="9" height="12" viewBox="0 0 8 10"><path d="M4 0a4 4 0 0 0-4 4c0 3 4 6 4 6s4-3 4-6a4 4 0 0 0-4-4zm0 5.5A1.5 1.5 0 1 1 4 2.5a1.5 1.5 0 0 1 0 3z" fill="#555"/></svg>Mountain View, California</div>
        <div class="status"><span class="badge full">Full Time</span>Posted 5 years ago</div>
      </div>
      <div class="job-row">
        <div class="logo-box">Tempova</div>
        <div class="info"><strong>Front-End Engineer</strong><small><b>Tempova</b> Analytics and Insights for the Music Industry</small></div>
        <div class="loc"><svg width="9" height="12" viewBox="0 0 8 10"><path d="M4 0a4 4 0 0 0-4 4c0 3 4 6 4 6s4-3 4-6a4 4 0 0 0-4-4zm0 5.5A1.5 1.5 0 1 1 4 2.5a1.5 1.5 0 0 1 0 3z" fill="#555"/></svg>Stanford, California</div>
        <div class="status"><span class="badge">Freelance</span>Posted 5 years ago</div>
      </div>
    </div>
  </section>
</main>

<section class="question-band">
  <h2>Got a question?</h2>
  <p>We're here to help. Check out our FAQs, send us an email or call us at 1 (800) 420-1180</p>
</section>

<footer class="site-footer">
  <div class="footer-col footer-brand">
    <div class="brand">VELMORA IT</div>
    <p>Job Searching Just Got Easy. Use Hireway to run a hiring site and earn money in the process!</p>
  </div>
  <div class="footer-col sitemap">
    <h4>Site Map</h4>
    <ul>
      <li>Blog</li><li>Cart</li><li>Checkout</li><li>Companies</li><li>FAQ</li><li>Find A Job</li><li>Home</li><li>Login</li><li>Manage Jobs</li><li>My Account</li><li>Post A Job</li><li>Pricing</li><li>Privacy Policy</li><li>Sample Page</li><li>Shop</li><li>Sign Up</li><li>Terms and Conditions</li><li>Testimonials</li>
    </ul>
  </div>
  <div class="footer-col news">
    <h4>Recent News Articles</h4>
    <ul>
      <li>The Best (and Worst) Canadian Merchant Account Providers<small>March 29, 2016</small></li>
      <li>Do you have a job that the average person doesn't even know exists?<small>March 22, 2016</small></li>
      <li>Cloudharbor launches first Canadian data-centre in Toronto<small>February 22, 2016</small></li>
    </ul>
  </div>
  <div class="footer-col offices">
    <h4>Hireway Offices</h4>
    <p>Hireway Inc. 88 Alder Lane, Suite B-4 Brookfield, New York 10419</p>
    <p>Hireway Inc Canada. 212 Harrow St, Suite 7 Toronto, Ontario M5R 2K9</p>
  </div>
</footer>

<div class="footer-bar">
  <span class="copy">© 2017 Classic – All rights reserved</span>
  <span class="top"></span>
  <div class="icons"><span></span><span></span><span></span><span></span><span></span><span></span><span></span></div>
</div>

</body>
</html>
```